vireLattice "organisation chart"

We need a new Organisation Chart for our Company! We are actually in a Change-management-process and will Change from a hierarchical Organisation in to a Network Organisation. Therefor we need a new Organisation Chart.
The following departements must be visible and legible on the Chart:
Team Sales & Consulting
Team Productmanagement
Team Supply Chain
Team Human Resources
Team Smart Digital Development
Team Marketing & Communication
The title of the Chart ist «vireLattice»
The Colors of the back of the Chart must be: RGB 73/25/102 // Pantone 2627
The Colors for the different Teams should be:
Team Sales & Consulting (Pantone: 803/neon yellow = Background)
Team Productmanagement (Pantone: 804/neon orange = Background)
Team Supply Chain (Pantone: 802/neon green = Background)
Team Human Resources (Pantone: 801/neon blue = Background)
Team Smart Digital Development (Pantone: 805/neon red = Background)
Team Marketing & Communication (Pantone: 803/neon pink = Background)
See below (upload files) an example showing a self-made Chart ... :-)
Our font is: Univers LT Std // Please feel free to Combine the Fonts Colors with the background colors
It Company

```html
<!DOCTYPE html>
<html lang="en">
<head>
<meta charset="utf-8">
<title>vireLattice – Organisation Chart</title>
<link rel="stylesheet" href="https://fonts.googleapis.com/css2?family=Montserrat:wght@400;500;700&display=swap">
<style>
  :root {
    --brand-purple: rgb(73, 25, 102);
    --brand-purple-light: #56217a;
    --brand-purple-dark: #3c1454;
    --ink: #111111;
    --connector: #ffffff;
    --title-blue: #1a9fd3;
    --team-sales: #f7e814;
    --team-product: #f9aa4b;
    --team-supply: #5eba47;
    --team-hr: #189bcf;
    --team-digital: #f07077;
    --team-marketing: #e74c9c;
  }
  html, body {
    margin: 0;
    padding: 0;
    width: 1200px;
    height: 1200px;
    overflow: hidden;
    background: var(--brand-purple);
  }
  .canvas {
    position: relative;
    width: 1200px;
    height: 1200px;
    overflow: hidden;
    font-family: "Montserrat", sans-serif;
    background:
      radial-gradient(ellipse at 35% 30%, var(--brand-purple-light) 0%, transparent 60%),
      radial-gradient(ellipse at 70% 85%, var(--brand-purple-dark) 0%, transparent 55%),
      var(--brand-purple);
  }
  .chart {
    position: absolute;
    inset: 0;
    width: 1200px;
    height: 1200px;
  }
  .chart-title {
    font-family: "Montserrat", sans-serif;
    font-weight: 700;
    font-size: 104px;
    fill: var(--title-blue);
  }
  .team-label {
    font-family: "Montserrat", sans-serif;
    font-weight: 500;
    font-size: 27px;
    fill: var(--ink);
    letter-spacing: 0.8px;
  }
  .link {
    fill: none;
    stroke: var(--connector);
  }
  .link-curve { stroke-width: 7; }
  .link-spoke { stroke-width: 5; }
  .hex-sales { fill: var(--team-sales); }
  .hex-product { fill: var(--team-product); }
  .hex-supply { fill: var(--team-supply); }
  .hex-hr { fill: var(--team-hr); }
  .hex-digital { fill: var(--team-digital); }
  .hex-marketing { fill: var(--team-marketing); }
</style>
</head>
<body>
<div class="canvas">
  <svg class="chart" viewBox="0 0 1300 1300" xmlns="http://www.w3.org/2000/svg">
    <defs>
      <polygon id="hexagon" points="-127,0 -63,-110 63,-110 127,0 63,110 -63,110"/>
      <marker id="arrowhead" viewBox="0 0 10 10" refX="8" refY="5"
              markerWidth="26" markerHeight="26" markerUnits="userSpaceOnUse"
              orient="auto-start-reverse">
        <path d="M0,0 L10,5 L0,10 Z" fill="#ffffff"/>
      </marker>
    </defs>

    <text class="chart-title" x="268" y="210" textLength="812" lengthAdjust="spacingAndGlyphs">vireLattice</text>

    <g class="network-links">
      <path class="link link-curve" d="M538,357 Q405,360 368,462" marker-start="url(#arrowhead)" marker-end="url(#arrowhead)"/>
      <path class="link link-curve" d="M752,355 Q885,360 925,458" marker-start="url(#arrowhead)" marker-end="url(#arrowhead)"/>
      <path class="link link-curve" d="M1040,638 Q1092,740 1036,836" marker-start="url(#arrowhead)" marker-end="url(#arrowhead)"/>
      <path class="link link-curve" d="M925,1026 Q890,1126 752,1128" marker-start="url(#arrowhead)" marker-end="url(#arrowhead)"/>
      <path class="link link-curve" d="M537,1138 Q402,1130 365,1030" marker-start="url(#arrowhead)" marker-end="url(#arrowhead)"/>
      <path class="link link-curve" d="M252,638 Q198,740 258,836" marker-start="url(#arrowhead)" marker-end="url(#arrowhead)"/>

      <path class="link link-spoke" d="M643,562 L643,922" marker-start="url(#arrowhead)" marker-end="url(#arrowhead)"/>
      <path class="link link-spoke" d="M487,655 L803,830" marker-start="url(#arrowhead)" marker-end="url(#arrowhead)"/>
      <path class="link link-spoke" d="M797,652 L485,835" marker-start="url(#arrowhead)" marker-end="url(#arrowhead)"/>
    </g>

    <g class="team team-sales">
      <use href="#hexagon" class="hex-sales" x="643" y="427"/>
      <text class="team-label" text-anchor="middle">
        <tspan x="643" y="418">Team Sales &amp;</tspan>
        <tspan x="650" y="450">Consulting</tspan>
      </text>
    </g>

    <g class="team team-product">
      <use href="#hexagon" class="hex-product" x="913" y="584"/>
      <text class="team-label" text-anchor="middle">
        <tspan x="911" y="547">Team</tspan>
        <tspan x="917" y="579">Product</tspan>
        <tspan x="917" y="611">management</tspan>
      </text>
    </g>

    <g class="team team-supply">
      <use href="#hexagon" class="hex-supply" x="913" y="896"/>
      <text class="team-label" text-anchor="middle">
        <tspan x="915" y="904">Team Supply</tspan>
        <tspan x="920" y="936">Chain</tspan>
      </text>
    </g>

    <g class="team team-hr">
      <use href="#hexagon" class="hex-hr" x="643" y="1051"/>
      <text class="team-label" text-anchor="middle">
        <tspan x="641" y="1022">Team</tspan>
        <tspan x="641" y="1054">Human</tspan>
        <tspan x="646" y="1086">Resources</tspan>
      </text>
    </g>

    <g class="team team-digital">
      <use href="#hexagon" class="hex-digital" x="371" y="896"/>
      <text class="team-label" text-anchor="middle">
        <tspan x="367" y="873">Team</tspan>
        <tspan x="368" y="905">Smart Digital</tspan>
        <tspan x="372" y="937">Development</tspan>
      </text>
    </g>

    <g class="team team-marketing">
      <use href="#hexagon" class="hex-marketing" x="371" y="584"/>
      <text class="team-label" text-anchor="middle">
        <tspan x="366" y="543">Team</tspan>
        <tspan x="366" y="572">Marketing &amp;</tspan>
        <tspan x="371" y="601">Communication</tspan>
      </text>
    </g>
  </svg>
</div>
</body>
</html>
```